Existing Plorv Website Redesign

Our current website is in need of redesign for the plorv.com platform. https://www.kestrawanders.com.au/ <br/>In addition to the brief below, we need the Website to be Multi – Lingual : English, Japanese, German, Dutch, French, Italian, Chinese Mandarin and Chinese Cantonese & Korean<br/><br/>All the content is already listed on the website. The successful design will implement the website with the current content and edit this including correct headers and URL addresses.<br/><br/>Company Profile-<br/>Kestra Wanders enhances the travellers' life experience through the wonder, discovery, adventure and cultural immersion of high quality tours throughout Papua New Guinea.<br/><br/>Our mission is to design and conduct safe, educational and exciting tours which:<br/><br/>cater for a range of ages, interests and budgets; respect local communities; promote sustainable tourism, leaving with them special memories.<br/><br/> <br/><br/>The current target demographic for Kestra Wanders of Papua New Guinea is the 50+ age group, primarily in Australia and New Zealand, but also the United States, Japan, Europe (Germany, France Italy & Britain and also China as it’s outbound visitor market matures and seeks new adventures.<br/><br/>We offer fully escorted small group tours and holidays that are safe, fully organised and guided for all age groups, nationalities and budgets.<br/><br/>PNG is uniquely placed as an attractive destination, showcasing the oldest, authentic surviving culture on earth! <br/><br/>Over 800 tribes generously share their customs, art, music, carvings, costumes and dances at a range of Festivals or “sing sings” held across the highlands and islands of this most picturesque of countries providing visiting culture enthusiasts and photographers with lasting memories and vivid images. Traversing the Pacific’s “Rim of Fire”, visitors are presented with a daily feast of scenery with the best nature has to offer amongst it’s big mountainous jungles and forests, untamed rivers, volcanic landscapes and pristine marine environments. Photograph animals, plants and exotic birds including the globally renowned Birds of Paradise.<br/><br/>The key group to target amongst the over 50’s are the Baby Boomers who are those born between 1946 to 1964.<br/><br/> <br/><br/>Baby boomers are also seeking an authentic experience whilst travelling. They want to go where the locals go, immersing themselves fully to experience and learn about a new culture.<br/><br/>According to the Global Voyaging Council, boomers are more likely to seek out educational and cultural experiences. What boomers really want is to be intellectually stimulated, which is why an experienced, knowledgeable and well-trained guide, such as Mark Delriss and those guides that he trains are necessary to attract them to these tours. Mark has immersed himself in the many periods of colonial occupier history along with a sound understanding of the first peoples and their cultures and Melanesian lifestyles.<br/><br/>As a destination Papua New Guinea will attract the baby boomers that are “young at heart” who actively seek out adventure, sometimes as a form of self-discovery. Knowing that they want to experience new adventures while being safe, Kestra Wanders has created adventure in a semi-controlled environment for the baby boomer.<br/><br/>Kestra Wanders of Papua New Guinea will be of interest primarily to the “Baby Boomer” demographic in Australia, many who have a fond familiarity with their neighbouring ex-colony. Their parents may have been involved in PNG in the pre-independence era as First and Second World War military personal, “Kiap” patrol officers, nurses, teachers,missionaries, tradesmen or public servants.<br/><br/>Potential visitors will discover a little known destination where the traditional Melanesian culture with over 800 tribes and languages, thrive and where, outside the major regional centres, little has changed in thousands of years.

Target Market(s)

Travel and Tourism

Colors

Designer to choose colors to be used in the design.

Requirements
Must have
• Website to be Multi – Lingual : English, Japanese, German, Dutch, French, Italian, Chinese Mandarin and Chinese Cantonese & Korean
• The successful design will implement the website with the current content and edit this including correct headers and URL addresses.

```html
<!DOCTYPE html>
<html lang="en">
<head>
<meta charset="utf-8">
<title>Kestra Wanders of Papua New Guinea</title>
<link href="https://fonts.googleapis.com/css2?family=Marcellus&family=Montserrat:wght@400;500;600;700;800&family=Lora:wght@400;600&display=swap" rel="stylesheet">
<style>
:root{
  --green-dark:#263f17;
  --green:#2f4b1f;
  --green-nav:#3a5628;
  --ink:#333;
  --muted:#777;
  --line:#cfcfcf;
  --footer:#2d2d2d;
  --footer-bar:#262626;
  --white:#fff;
}
*{box-sizing:border-box;margin:0;padding:0}
html,body{width:1200px;height:4066px;overflow:hidden}
body{position:relative;background:var(--white);font-family:"Montserrat",sans-serif;color:var(--ink)}
.abs{position:absolute}
.ph{position:absolute;display:block}

/* top bar */
.topbar{left:0;top:0;width:1200px;height:57px;background:#fff;border-bottom:2px solid #e4e4e4}
.topbar .phone{left:95px;top:17px;font-family:"Lora",serif;font-size:20px;color:#333;display:flex;align-items:center;gap:10px}
.social{width:32px;height:32px;border-radius:50%;background:var(--green);top:13px}
.login{left:730px;top:12px;display:flex;align-items:center;gap:10px;font-size:12px;font-weight:700}
.login .ring{width:32px;height:32px;border-radius:50%;border:2px solid #222}
.lang{left:850px;top:15px;display:flex;align-items:center;gap:6px}
.lang .dot{width:28px;height:28px;border-radius:50%;background:#c9d3e6}
.search{left:932px;top:10px;width:168px;height:34px;border:1px solid #e3e3e3;background:#fff}
.search svg{position:absolute;right:10px;top:9px}

/* header */
.header{left:0;top:70px;width:1200px;height:127px;background:var(--green-nav)}
.brand{left:90px;top:98px;display:flex;align-items:center;gap:12px;font-family:"Marcellus",serif;color:#fff;font-size:34px}
.brand .mark{width:44px;height:44px;border:2px solid #fff;border-radius:50%}
.nav{right:98px;top:119px;display:flex;gap:42px;font-size:14px;font-weight:700;color:#fff}
.nav a{color:#fff;text-decoration:none;position:relative}
.nav a.active:after{content:"";position:absolute;left:0;right:0;bottom:-14px;height:2px;background:#fff}

/* hero */
.hero{left:0;top:197px;width:1200px;height:680px;background:linear-gradient(180deg,#a9c4dc 0%,#6f9b6f 22%,#48b1c0 36%,#8c7a62 60%,#d9d1c0 100%)}
.hero-panel{left:216px;top:262px;width:768px;height:420px;background:rgba(80,80,80,.45)}
.hero-title{left:216px;width:768px;top:359px;text-align:center;font-family:"Montserrat",sans-serif;font-weight:800;font-size:31px;line-height:40px;color:#fff;letter-spacing:.5px}
.hero-sub{left:216px;width:768px;top:418px;text-align:center;font-weight:700;font-size:15px;color:#fff;line-height:31px}
.btn-hero{left:486px;top:529px;width:228px;height:58px;background:var(--green);color:#fff;font-family:"Marcellus",serif;font-size:21px;display:flex;align-items:center;justify-content:center}

.sec-title{left:0;width:1200px;text-align:center;font-family:"Marcellus",serif;font-size:34px;color:#2b2b2b;display:flex;justify-content:center;align-items:center;gap:20px}
.sec-title:before,.sec-title:after{content:"";width:97px;height:1px;background:#333}
.sec-title.light{color:#fff}
.sec-title.light:before,.sec-title.light:after{background:#fff;width:120px}

/* about */
.about-text{left:110px;width:980px;top:903px;text-align:center;font-size:16px;line-height:31px;color:#444}
.btn-dark{left:502px;top:1061px;width:196px;height:58px;background:var(--green-dark);color:#fff;font-size:15px;font-weight:600;display:flex;align-items:center;justify-content:center;border-radius:4px}

/* destinations */
.dest-band{left:0;top:1173px;width:1200px;height:567px;background:linear-gradient(160deg,#6f7d55,#9aa077 40%,#5c6e44 70%,#8a8c6a)}
.card{top:1295px;width:297px;height:395px;background:#fff;border:2px solid #ececec}
.card .ph{left:0;top:0;width:293px;height:220px}
.card h3{position:absolute;top:245px;width:100%;text-align:center;font-family:"Marcellus",serif;font-size:17px;font-weight:400;color:#333}
.card p{position:absolute;top:267px;left:22px;right:22px;text-align:center;font-family:"Lora",serif;font-size:12px;line-height:19px;color:#888}
.card .meta{position:absolute;left:0;right:0;bottom:0;height:48px;border-top:1px solid #ddd;display:flex;font-family:"Lora",serif;font-size:12px;color:#444}
.card .meta span{display:flex;align-items:center;justify-content:center;border-right:1px solid #ddd}
.card .meta span:nth-child(1){width:90px}
.card .meta span:nth-child(2){width:108px}
.card .meta span:nth-child(3){flex:1;border:0;font-family:"Montserrat",sans-serif;font-weight:700;color:var(--green)}

/* blogs */
.blog-main{left:95px;top:1874px;width:497px;height:305px;border:3px solid var(--green)}
.blog-h{font-family:"Lora",serif;color:var(--green-dark)}
.read{display:flex;align-items:center;gap:16px;font-weight:700;color:var(--green-dark);font-size:15px}
.read i{width:26px;height:26px;border:2px solid #333;border-radius:50%;display:flex;align-items:center;justify-content:center;font-style:normal}
.blog-side .ph{width:245px;height:149px}
.side-text{left:876px;width:230px}
.side-text h4{font-family:"Lora",serif;font-weight:400;font-size:16px;color:var(--green-dark)}
.side-text p{margin-top:12px;font-family:"Lora",serif;font-size:10.5px;line-height:17px;color:#888}
.side-text .read{margin-top:14px}
.rule{left:614px;width:489px;height:2px;background:#ccc}

/* gallery */
.gal-bg{left:0;top:2915px;width:1200px;height:725px;background:linear-gradient(180deg,#7aa8c8 0%,#a8c6d8 45%,#d9e4e6 70%,#b6c6a5 100%)}
.tile{width:330px;height:328px}

/* newsletter */
.nl-title{left:226px;top:3507px;color:#fff;font-family:"Marcellus",serif}
.nl-title .a{font-size:21px;letter-spacing:1px}
.nl-title .b{font-size:28px;letter-spacing:1px}
.nl-icon{left:150px;top:3505px}
.field{background:#fff;border:1px solid #ddd;font-family:"Lora",serif;font-size:15px;color:#999;padding:0 10px;display:flex;align-items:center}
.btn-grey{background:#9a9a9a;color:#fff;font-size:16px;font-family:"Lora",serif;display:flex;align-items:center;justify-content:center}

/* footer */
.footer{left:0;top:3640px;width:1200px;height:366px;background:var(--footer)}
.f-title{font-size:20px;font-weight:500;color:#fff}
.f-link{font-size:15px;font-weight:600;color:#fff}
.f-info{font-size:13.5px;font-weight:600;color:#fff;line-height:21px}
.map{left:761px;top:3821px;width:344px;height:115px;background:linear-gradient(135deg,#c9ddef,#e9eef0 50%,#cfe0ee)}
.bottombar{left:0;top:4006px;width:1200px;height:60px;background:var(--footer-bar);border-top:2px solid #fff}
.bottombar .l{left:97px;top:18px;font-family:"Lora",serif;font-weight:600;color:#fff;font-size:17px}
.bottombar .r{right:97px;top:18px;font-family:"Lora",serif;font-weight:600;color:#fff;font-size:17px}
</style>
</head>
<body>

<!-- top bar -->
<div class="abs topbar">
  <div class="abs phone">
    <svg width="18" height="18" viewBox="0 0 24 24"><path fill="#2f4b1f" d="M6.6 10.8a15 15 0 0 0 6.6 6.6l2.2-2.2c.3-.3.7-.4 1-.2 1.1.4 2.3.6 3.6.6.6 0 1 .4 1 1V20c0 .6-.4 1-1 1A17 17 0 0 1 3 4c0-.6.4-1 1-1h3.5c.6 0 1 .4 1 1 0 1.3.2 2.5.6 3.6.1.3 0 .7-.2 1z"/></svg>
    +61 400 372 915
  </div>
  <div class="abs social" style="left:568px"></div>
  <div class="abs social" style="left:623px"></div>
  <div class="abs social" style="left:678px"></div>
  <div class="abs login"><span class="ring"></span>LOGIN</div>
  <div class="abs lang"><span class="dot"></span>
    <svg width="14" height="9" viewBox="0 0 14 9"><path d="M0 0h14L7 9z" fill="#222"/></svg></div>
  <div class="abs search"><svg width="16" height="16" viewBox="0 0 24 24"><circle cx="10" cy="10" r="7" stroke="#222" stroke-width="3" fill="none"/><path d="M15 15l7 7" stroke="#222" stroke-width="3"/></svg></div>
</div>

<!-- header -->
<div class="abs header"></div>
<div class="abs brand"><span class="mark"></span>Kestra Wanders</div>
<nav class="abs nav">
  <a class="active">Home</a><a>Tours</a><a>Birdwatching</a><a>Gallery</a><a>About Us</a><a>Contact</a>
</nav>

<!-- hero -->
<div class="abs hero" role="img" aria-label="Photo of villagers beside carved outrigger canoes on a tropical beach"></div>
<div class="abs hero-panel"></div>
<h1 class="abs hero-title">WELCOME TO KESTRA WANDERS</h1>
<div class="abs hero-sub">FULLY ESCORTED SMALL GROUP TOURS<br>SAFE ADVENTURES OF PAPUA NEW GUINEA</div>
<div class="abs btn-hero">CONTACT US</div>
<svg class="abs" style="left:0;top:700px" width="1200" height="180" viewBox="0 0 1200 180">
  <path d="M0 35 C120 10 300 30 520 40 C800 50 1000 40 1200 160 L1200 180 L0 180 Z" fill="#fff"/>
  <path d="M0 35 C120 10 300 30 520 40 C800 50 1000 40 1200 160 L1200 175 C1000 60 800 64 520 56 C300 46 120 30 0 72 Z" fill="#2f4b1f"/>
</svg>

<!-- about -->
<div class="abs sec-title" style="top:828px">ABOUT US</div>
<p class="abs about-text">Kestra Wanders is a tour operator specialising in Papua New Guinea and also Japan. All our destinations offer the ultimate experience for excitement, fun, adventure and cultural interaction. Come and discover the ancient lands and first peoples, experiencing up close the vividly spectacular and varied forms of customs, art, costumes and cuisine in the most culturally intact places in the world.</p>
<div class="abs btn-dark">READ MORE</div>

<!-- destinations -->
<div class="abs dest-band" role="img" aria-label="Aerial photo of a winding road through green hills"></div>
<div class="abs sec-title light" style="top:1228px">POPULAR DESTINATION</div>

<div class="abs card" style="left:110px">
  <div class="ph" role="img" aria-label="Photo of a highland dancer in a feathered headdress" style="background:linear-gradient(160deg,#3c6fbf,#8b2b1e 55%,#5a3a22)"></div>
  <h3>NEW BRITAIN ISLAND</h3>
  <p>Sed ut perspiciatis unde omnis iste natus error sit voluptatem accusantium dolorem que laudantium, totam rem aperiam,</p>
  <div class="meta"><span>▦ 9 DAYS</span><span>7,000 USD P.P</span><span>Read More</span></div>
</div>
<div class="abs card" style="left:450px">
  <div class="ph" role="img" aria-label="Photo of a cassowary bird" style="background:linear-gradient(150deg,#8a6a35,#3b3f3a 50%,#9d7b45)"></div>
  <h3>NEW BRITAIN &amp; EAST SEPIK</h3>
  <p>Sed ut perspiciatis unde omnis iste natus error sit voluptatem accusantium dolorem que laudantium, totam rem aperiam,</p>
  <div class="meta"><span>▦ 9 DAYS</span><span>7,000 USD P.P</span><span>Read More</span></div>
</div>
<div class="abs card" style="left:790px">
  <div class="ph" role="img" aria-label="Photo of a red pagoda in a forested Japanese valley" style="background:linear-gradient(180deg,#2f78c9,#3e7a3c 45%,#2d5a2a)"></div>
  <h3>JAPAN</h3>
  <p>Sed ut perspiciatis unde omnis iste natus error sit voluptatem accusantium dolorem que laudantium, totam rem aperiam,</p>
  <div class="meta"><span>▦ 9 DAYS</span><span>7,000 USD P.P</span><span>Read More</span></div>
</div>

<!-- blogs -->
<div class="abs sec-title" style="top:1781px">OUR BLOGS</div>
<div class="abs blog-main" role="img" aria-label="Photo of paddlers in a wooden canoe on blue water" style="background:linear-gradient(180deg,#a8bccb,#4d6f8f 45%,#163e7a)"></div>
<h3 class="abs blog-h" style="left:95px;top:2202px;font-size:26px;font-weight:400">Lorem ipsum dolor sit amet</h3>
<p class="abs" style="left:95px;top:2250px;width:480px;font-family:'Lora',serif;font-size:15px;line-height:31px;color:#555">Sed ut perspiciatis unde omnis iste natus error sit voluptatem accusantium doloremque laudantium, totam rem aperiam, eaque ipsa quae ab illo inventore veritatis et quasi architecto beatae vitae dicta sunt explicabo. Nemo enim ipsam volupta quia voluptas sit aspernatur aut odit aut fugit, sed quia .</p>
<div class="abs read" style="left:95px;top:2418px">Read More <i>→</i></div>

<div class="blog-side">
  <div class="ph" style="left:614px;top:1874px;background:linear-gradient(135deg,#3a2b1c,#c9a227 50%,#1e1a14)" role="img" aria-label="Photo of painted faces in tribal costume"></div>
  <div class="ph" style="left:614px;top:2078px;background:linear-gradient(135deg,#4a3a25,#d86a1f 50%,#6b4a2a)" role="img" aria-label="Photo of a bird of paradise on a branch"></div>
  <div class="ph" style="left:614px;top:2280px;background:linear-gradient(180deg,#b0c2cc,#4d6f8f 55%,#1d4680)" role="img" aria-label="Photo of canoe paddlers at sea"></div>
</div>
<div class="abs side-text" style="top:1876px"><h4>Lorem ipsum dolor sit amet</h4><p>Sed ut perspiciatis unde omnis iste natus error sit voluptatem accusantium dolorem que laudantium, totam rem aperiam, eaque ipsa quae ab illo inventore veritatis et</p><div class="read">Read More <i>→</i></div></div>
<div class="abs side-text" style="top:2080px"><h4>Lorem ipsum dolor sit amet</h4><p>Sed ut perspiciatis unde omnis iste natus error sit voluptatem accusantium dolorem que laudantium, totam rem aperiam, eaque ipsa quae ab illo inventore veritatis et</p><div class="read">Read More <i>→</i></div></div>
<div class="abs side-text" style="top:2282px"><h4>Lorem ipsum dolor sit amet</h4><p>Sed ut perspiciatis unde omnis iste natus error sit voluptatem accusantium doloremque laudantium, totam rem aperiam, eaque ipsa quae ab illo inventore veritatis et</p><div class="read">Read More <i>→</i></div></div>
<div class="abs rule" style="top:2049px"></div>
<div class="abs rule" style="top:2252px"></div>
<div class="abs rule" style="top:2456px"></div>

<!-- gallery -->
<div class="abs gal-bg" role="img" aria-label="Background photo of a Japanese pagoda and mountain under a blue sky"></div>
<div class="abs sec-title" style="top:2512px">PHOTO GALLERY</div>
<div class="ph tile" style="left:93px;top:2602px;background:linear-gradient(160deg,#8a3fa0,#b07050 45%,#5a3a28)" role="img" aria-label="Photo of a smiling child in a feathered headdress"></div>
<div class="ph tile" style="left:434px;top:2602px;background:linear-gradient(135deg,#3a2a20,#b58a5a 50%,#2a2a2a)" role="img" aria-label="Photo of carved painted wooden masks"></div>
<div class="ph tile" style="left:774px;top:2602px;background:linear-gradient(150deg,#8a6a35,#343934 50%,#9d7b45)" role="img" aria-label="Photo of a cassowary bird"></div>
<div class="ph tile" style="left:93px;top:2940px;background:linear-gradient(180deg,#aebfcd,#6e7468 50%,#2e5a74)" role="img" aria-label="Photo of a rocky limestone island in the sea"></div>
<div class="ph tile" style="left:434px;top:2940px;background:linear-gradient(160deg,#6e8a3a,#2a2a2a 50%,#9aa04a)" role="img" aria-label="Photo of a costumed dancer with leaf headdress"></div>
<div class="ph tile" style="left:774px;top:2940px;background:linear-gradient(180deg,#9ab4c8,#4d6f8f 50%,#1d4680)" role="img" aria-label="Photo of canoe paddlers at sea"></div>
<svg class="abs" style="left:0;top:3270px" width="1200" height="372" viewBox="0 0 1200 372">
  <path d="M0 0 C120 60 220 110 420 110 C640 110 760 70 980 95 C1080 105 1150 130 1200 160 L1200 372 L0 372 Z" fill="#263f17"/>
</svg>

<!-- newsletter -->
<svg class="abs nl-icon" width="68" height="66" viewBox="0 0 68 66"><path d="M4 36 L42 4 L64 30 L26 62 Z" fill="#fff"/><path d="M4 36 L34 40 L64 30" stroke="#263f17" stroke-width="3" fill="none"/></svg>
<div class="abs nl-title"><div class="a">NEWSLETTER</div><div class="b">SUBSCRIPTION</div></div>
<div class="abs field" style="left:493px;top:3513px;width:203px;height:48px">Enter Your Name</div>
<div class="abs field" style="left:706px;top:3513px;width:203px;height:48px">Enter Your Email</div>
<div class="abs btn-grey" style="left:919px;top:3513px;width:133px;height:48px">SUBSCRIBE</div>

<!-- footer -->
<div class="abs footer"></div>
<div class="abs f-title" style="left:98px;top:3685px">Contact Us</div>
<div class="abs field" style="left:95px;top:3731px;width:158px;height:38px">Name</div>
<div class="abs field" style="left:264px;top:3731px;width:158px;height:38px">Email</div>
<div class="abs field" style="left:95px;top:3790px;width:158px;height:38px">Phone</div>
<div class="abs field" style="left:264px;top:3790px;width:158px;height:38px">City</div>
<div class="abs field" style="left:95px;top:3850px;width:327px;height:39px">Message</div>
<div class="abs btn-grey" style="left:98px;top:3913px;width:114px;height:38px">SUBMIT</div>

<div class="abs f-title" style="left:537px;top:3685px">Links</div>
<div class="abs f-link" style="left:537px;top:3727px">Home</div>
<div class="abs f-link" style="left:537px;top:3774px">Our Tours</div>
<div class="abs f-link" style="left:537px;top:3821px">Contact Us</div>
<div class="abs f-link" style="left:537px;top:3867px">Gallery</div>
<div class="abs f-link" style="left:537px;top:3915px">Bird Watching</div>

<div class="abs f-title" style="left:761px;top:3685px">Contact Info</div>
<svg class="abs" style="left:761px;top:3744px" width="26" height="22" viewBox="0 0 26 22"><path d="M13 1 L25 11 H21 V21 H15 V15 H11 V21 H5 V11 H1 Z" fill="#fff"/></svg>
<div class="abs f-info" style="left:804px;top:3738px">P.O. Box 4417 Wattle Grove<br>3152 Melbourne</div>
<svg class="abs" style="left:762px;top:3786px" width="14" height="14" viewBox="0 0 24 24"><path fill="#fff" d="M6.6 10.8a15 15 0 0 0 6.6 6.6l2.2-2.2c.3-.3.7-.4 1-.2 1.1.4 2.3.6 3.6.6.6 0 1 .4 1 1V20c0 .6-.4 1-1 1A17 17 0 0 1 3 4c0-.6.4-1 1-1h3.5c.6 0 1 .4 1 1 0 1.3.2 2.5.6 3.6.1.3 0 .7-.2 1z"/></svg>
<div class="abs f-info" style="left:784px;top:3783px">+61 400 372 915</div>
<svg class="abs" style="left:920px;top:3787px" width="16" height="12" viewBox="0 0 16 12"><rect width="16" height="12" fill="#fff"/><path d="M0 0 L8 7 L16 0" stroke="#2d2d2d" stroke-width="1.5" fill="none"/></svg>
<div class="abs f-info" style="left:947px;top:3781px">info@kestrawanders.com</div>
<div class="abs map" role="img" aria-label="Map showing Papua New Guinea and surrounding region"></div>

<div class="abs bottombar">
  <div class="abs l">Copyright © 2019 Kestra Wanders</div>
  <div class="abs r">Terms &amp; Conditions | Privacy Policy</div>
</div>

</body>
</html>
```